Front & Back Book Cover Design

Title:
THE QUIET LANDLORD: How to Grow Comfort and Plenty Through Property Held by Others
Author:
Mel T. Varnak
Design Philosophy:
A modern, minimalist-luxury aesthetic that feels visionary and intelligent — positioned between business innovation (The Brisk Venture), modern finance (The Anatomy of Thrift), and timeless real estate insight (Bold Aunt Meek Aunt).
Think: clean, bold, and idea-driven — a visual reflection of the book’s central concept: wealth through clarity, not clutter.
Back Cover:
To include book description along with author photo and bio
Files:
PNG, PDF, EPUB

```html
<!DOCTYPE html>
<html lang="en">
<head>
<meta charset="utf-8">
<title>The Quiet Landlord — Back Cover</title>
<link href="https://fonts.googleapis.com/css2?family=Oswald:wght@400;500&family=Yanone+Kaffeesatz:wght@300;400;600&display=swap" rel="stylesheet">
<style>
  :root {
    --green: #8bc168;
    --green-deep: #7aae5a;
    --green-light: #96c874;
    --ink: #454647;
    --white: #ffffff;
    --photo-dark: #2e2e30;
    --photo-mid: #6b6a66;
  }
  * { margin: 0; padding: 0; box-sizing: border-box; }
  html, body { width: 743px; height: 1200px; overflow: hidden; }
  body {
    position: relative;
    background:
      linear-gradient(172deg, transparent 0 58%, rgba(122,174,90,.35) 62%, transparent 70%),
      linear-gradient(176deg, rgba(122,174,90,.55) 0%, rgba(139,193,104,0) 16%),
      linear-gradient(180deg, transparent 0 86%, rgba(150,200,116,.5) 92%, transparent 100%),
      var(--green);
    color: var(--white);
    font-family: "Yanone Kaffeesatz", "Arial Narrow", sans-serif;
    font-weight: 300;
  }
  .back-cover { position: absolute; inset: 0; }
  .intro, .discover, .about {
    position: absolute;
    left: 40px; right: 40px;
    text-align: center;
  }
  .intro { top: 64px; font-size: 17.5px; line-height: 23.6px; }
  .section-heading {
    font-family: "Oswald", "Arial Narrow", sans-serif;
    font-weight: 400;
    color: var(--ink);
    font-size: 25px;
    line-height: 30px;
    letter-spacing: .2px;
  }
  .discover { top: 212px; }
  .discover .list { font-size: 17.5px; line-height: 23.6px; margin-top: 0; }
  .discover .closing { font-weight: 400; }
  .about { top: 527px; }
  .about .bio {
    font-weight: 600;
    font-size: 17.5px;
    line-height: 23.6px;
    margin-top: 3px;
  }
  .author-photo {
    position: absolute;
    left: 68px; top: 781px;
    width: 273px; height: 350px;
    background:
      radial-gradient(ellipse 40% 55% at 55% 70%, #1f1f21 0 60%, transparent 61%),
      linear-gradient(180deg, #4a4a4a 0%, var(--photo-mid) 45%, var(--photo-dark) 100%);
  }
  .title-block {
    position: absolute;
    left: 373px; top: 776px;
    color: var(--ink);
    font-family: "Oswald", "Arial Narrow", sans-serif;
  }
  .title-block .title { font-size: 31px; line-height: 40px; font-weight: 500; }
  .title-block .subtitle { font-size: 29px; line-height: 41.5px; font-weight: 400; margin-top: 1px; }
  .title-block .byline { font-size: 50px; line-height: 60px; font-weight: 500; margin-top: 58px; }
</style>
</head>
<body>
<main class="back-cover">
  <section class="intro">
    What if the smartest real estate investors in the world don’t actually own anything?<br>
    In a world where leverage has replaced labor and access has replaced assets,<br>
    The Quiet Landlord reveals how a new generation of entrepreneurs is building wealth without<br>
    deeds, mortgages, or massive capital. Mel T. Varnak exposes the hidden playbook behind modern real<br>
    estate wealth — not through ownership, but through control, creativity, and influence.
  </section>

  <section class="discover">
    <h2 class="section-heading">YOU WILL DISCOVER HOW TO:</h2>
    <p class="list">
      Profit from properties you never buy through partnerships, performance models, and control<br>
      agreements. Monetize your skills, systems, and relationships just like institutional investors do.<br>
      Build digital real estate — brands, websites, and lead funnels that pay like rentals.<br>
      Create recurring income through master leases, management contracts, and service-based equity.<br>
      Design your freedom formula — where wealth is measured in time, not titles. Packed with<br>
      frameworks, examples, and the mindset of modern deal-makers,<br>
      The Quiet Landlord is a blueprint for the future of wealth creation — one built on access,<br>
      not assets.<br>
      Because in the new economy, the most powerful investors don’t own real estate.<br>
      <span class="closing">They own opportunity. And now, you can too.</span>
    </p>
  </section>

  <section class="about">
    <h2 class="section-heading">ABOUT THE AUTHOR</h2>
    <p class="bio">
      Mel T. Varnak is a real estate entrepreneur and owner of Halvercrest Designs in Las Vegas, NV<br>
      and Parkline Realty Summit in Ventura, California. Combining design, development, and deal<br>
      strategy, he’s helped agents, investors, and entrepreneurs build freedom through<br>
      systems — not stuff. The Quiet Landlord is his definitive guide to building wealth through<br>
      creative control.
    </p>
  </section>

  <div class="author-photo" role="img" aria-label="Author portrait: man in a dark blazer and white T-shirt in a modern office"></div>

  <section class="title-block">
    <h1 class="title">THE QUIET LANDLORD</h1>
    <p class="subtitle">How to Grow Comfort and<br>Plenty Through Property<br>Held by Others</p>
    <p class="byline">by MEL T. VARNAK</p>
  </section>
</main>
</body>
</html>
```